Tech Savy small Business accountant business card design

We need a business card for a new company based in the cloud. We provide tax, business advisory, accounting, information technology solutions and back office functions to small businesses. We offer fixed fee packages with add on services as you need them. By harnessing technology we simplify small business operational processes providing valuable time and information for small business owners to grow their business. In the logo (zulvarine) we want to be able to see zulv and experts. The final design should communicate achieving growth dreams and balance (ie life and $).
Updates
This project has been temporarily placed on hold until I finalize "Tech Savy small Business accountant needs a logo". I invite all designers to submit on this logo project. Once my logo is finalized I will resume this business card contest. Thanks Added Wednesday, March 19, 2014
This project has been temporarily placed on hold until I finalize "Tech Savy small Business accountant logo". I invite all designers to submit on this logo project. Once my logo is finalized I will resume this business card contest. Thanks Added Thursday, March 20, 2014
Target Market(s)
Small Business (Revenue $500,000, more than 3 employees) owners.
Industry/Entity Type
Small Business
Contact Information for Business Card
Marla Pennick (Principal)
Accountant, Tax Agent.
TEL | 0417 583 916
EMAIL | Marla.Pennick@zulvarine.com.au
WEB | www.zulvarine.com.au
Look and feel

```html
<!DOCTYPE html>
<html lang="en">
<head>
<meta charset="utf-8">
<title>zulvarine business card</title>
<link href="https://fonts.googleapis.com/css2?family=Barlow:wght@300;400;600&family=Barlow+Condensed:wght@400;600&display=swap" rel="stylesheet">
<style>
  :root {
    --blue: #1b92d6;
    --grey: #626468;
    --grey-dark: #55585c;
    --white: #ffffff;
    --tag-light: #d9dadc;
    --page: #c9cacc;
  }
  html, body {
    margin: 0;
    width: 1200px;
    height: 1200px;
    overflow: hidden;
    background: var(--page);
  }
  .canvas {
    position: relative;
    width: 1200px;
    height: 1200px;
  }
  .card {
    position: absolute;
    left: 160px;
    width: 880px;
    height: 520px;
    background: var(--white);
    overflow: hidden;
    box-shadow: 0 6px 18px rgba(0,0,0,0.18);
  }
  .card--back { top: 50px; }
  .card--front { top: 630px; }
  .card__bands {
    position: absolute;
    inset: 0;
    width: 880px;
    height: 520px;
  }
  .brand {
    position: absolute;
    font-family: "Barlow", sans-serif;
    font-weight: 600;
    letter-spacing: -3px;
    line-height: 1;
  }
  .tagline {
    position: absolute;
    font-family: "Barlow", sans-serif;
    font-weight: 400;
    line-height: 1;
  }
  .card--back .brand {
    left: 200px;
    top: 170px;
    font-size: 130px;
    color: var(--white);
  }
  .card--back .tagline {
    left: 252px;
    top: 310px;
    font-size: 30px;
    color: var(--tag-light);
  }
  .card--front .brand {
    right: 60px;
    top: 50px;
    font-size: 116px;
    color: var(--grey-dark);
  }
  .card--front .tagline {
    right: 60px;
    top: 180px;
    font-size: 27px;
    color: var(--grey-dark);
  }
  .holder {
    position: absolute;
    left: 50px;
    top: 262px;
    font-family: "Barlow Condensed", sans-serif;
    color: var(--white);
    white-space: nowrap;
  }
  .holder__name {
    font-size: 38px;
    font-weight: 600;
    text-transform: uppercase;
  }
  .holder__role {
    margin-left: 18px;
    font-size: 24px;
    font-weight: 400;
    text-transform: uppercase;
  }
  .contacts {
    position: absolute;
    left: 120px;
    top: 362px;
    margin: 0;
    padding: 0;
    list-style: none;
    font-family: "Barlow Condensed", sans-serif;
    font-size: 32px;
    color: var(--white);
  }
  .contacts__item {
    display: flex;
    align-items: center;
    height: 48px;
  }
  .contacts__icon {
    width: 24px;
    height: 24px;
    margin-right: 22px;
    flex: none;
  }
</style>
</head>
<body>
<main class="canvas">

  <section class="card card--back" aria-label="Card back">
    <svg class="card__bands" viewBox="0 0 880 520" aria-hidden="true">
      <rect x="0" y="0" width="880" height="128" fill="var(--blue)"/>
      <polygon points="0,142 310,142 326,128 342,142 880,142 880,380 520,380 504,394 488,380 0,380" fill="var(--grey)"/>
      <rect x="0" y="394" width="880" height="126" fill="var(--blue)"/>
      <polygon points="0,128 310,128 326,114 342,128 880,128 880,142 342,142 326,128 310,142 0,142" fill="var(--white)"/>
      <polygon points="0,380 488,380 504,394 520,380 880,380 880,394 520,394 504,408 488,394 0,394" fill="var(--white)"/>
    </svg>
    <div class="brand">zulvarine</div>
    <div class="tagline">Your business and accounting partner</div>
  </section>

  <section class="card card--front" aria-label="Card front">
    <svg class="card__bands" viewBox="0 0 880 520" aria-hidden="true">
      <polygon points="0,246 700,246 716,232 732,246 880,246 880,318 182,318 166,334 150,318 0,318" fill="var(--blue)"/>
      <polygon points="0,332 150,332 166,348 182,332 880,332 880,520 0,520" fill="var(--grey)"/>
    </svg>
    <div class="brand">zulvarine</div>
    <div class="tagline">Your business and accounting partner</div>
    <div class="holder">
      <span class="holder__name">Marla Pennick (Principal)</span><span class="holder__role">Accountant, Tax Agent</span>
    </div>
    <ul class="contacts">
      <li class="contacts__item">
        <svg class="contacts__icon" viewBox="0 0 24 24" aria-hidden="true"><path d="M6 3l4 4-2 3c1 2 4 5 6 6l3-2 4 4-3 3C10 21 3 14 3 6z" fill="var(--white)"/></svg>
        0417 583 916
      </li>
      <li class="contacts__item">
        <svg class="contacts__icon" viewBox="0 0 24 24" aria-hidden="true"><rect x="2" y="5" width="20" height="14" rx="1" fill="var(--white)"/><path d="M2 6l10 7 10-7" fill="none" stroke="var(--grey)" stroke-width="2"/></svg>
        Marla.Pennick@zulvarine.com.au
      </li>
      <li class="contacts__item">
        <svg class="contacts__icon" viewBox="0 0 24 24" aria-hidden="true"><circle cx="12" cy="12" r="10" fill="var(--white)"/><path d="M2 12h20M12 2c4 4 4 16 0 20M12 2c-4 4-4 16 0 20" fill="none" stroke="var(--grey)" stroke-width="1.5"/></svg>
        www.zulvarine.com.au
      </li>
    </ul>
  </section>

</main>
</body>
</html>
```